Professional Sales Business looking for inspirational poster

I need an inspirational poster design for sales professionals, targeted around the phrase "Win Fast, Lose Fast". The style of the poster will be primarily minimalistic and flat with the main focus being on the phrase, however, any graphics or creative font and background styles are encouraged. Color choice is up to you.

Design Specs:
Vector files are best. If creating a vector file isn't possible, 150dpi raster images (at actual size or bigger) are good too. The poster must be in a portrait layout and scalable to the sizes of 18" X 24" and 24" X 36". Please convert all text to outlines.

Please msg me if you have any additional questions.

```html
<!DOCTYPE html>
<html lang="en">
<head>
<meta charset="utf-8">
<title>Win Fast Lose Fast — Sales Poster</title>
<link rel="stylesheet" href="https://fonts.googleapis.com/css2?family=Josefin+Sans:wght@700&display=swap">
<style>
  :root {
    --bg-center: #ea5d7d;
    --bg-edge: #df1443;
    --ink-cream: #fffdf1;
    --ink-shadow: #b8002f;
  }
  html, body {
    margin: 0;
    padding: 0;
    width: 1200px;
    height: 900px;
    overflow: hidden;
  }
  .poster {
    width: 1200px;
    height: 900px;
    background: radial-gradient(circle at 50% 45%, var(--bg-center) 0%, var(--bg-edge) 85%);
    position: relative;
  }
  .poster__art {
    position: absolute;
    inset: 0;
    width: 1200px;
    height: 900px;
  }
  .headline {
    font-family: "Josefin Sans", "Arial Black", sans-serif;
    font-weight: 700;
  }
  .headline__face { fill: var(--ink-cream); }
  .headline__shadow { fill: var(--ink-shadow); }
  .rule { fill: var(--ink-cream); }
</style>
</head>
<body>
  <main class="poster">
    <svg class="poster__art" viewBox="0 0 1200 900" xmlns="http://www.w3.org/2000/svg">
      <rect class="rule rule--top" x="375" y="87" width="428" height="8"/>

      <g class="headline headline__shadow" aria-hidden="true">
        <text x="409" y="284" font-size="222" textLength="400" lengthAdjust="spacingAndGlyphs">WIN</text>
        <text x="439" y="429" font-size="152" textLength="355" lengthAdjust="spacingAndGlyphs">FAST</text>
        <text x="419" y="609" font-size="214" textLength="385" lengthAdjust="spacingAndGlyphs">LOSE</text>
        <text x="439" y="754" font-size="158" textLength="355" lengthAdjust="spacingAndGlyphs">FAST</text>
      </g>

      <g class="headline headline__face">
        <text x="395" y="280" font-size="222" textLength="400" lengthAdjust="spacingAndGlyphs">WIN</text>
        <text x="425" y="425" font-size="152" textLength="355" lengthAdjust="spacingAndGlyphs">FAST</text>
        <text x="405" y="605" font-size="214" textLength="385" lengthAdjust="spacingAndGlyphs">LOSE</text>
        <text x="425" y="750" font-size="158" textLength="355" lengthAdjust="spacingAndGlyphs">FAST</text>
      </g>

      <rect class="rule rule--bottom" x="375" y="775" width="428" height="8"/>
    </svg>
  </main>
</body>
</html>
```